Personal Training Studio Checkin App (or URL based)

I would like a simple web based app built for our  business. We have a training studio with a simple business model. All our clients buy sessions in packages either 4, 8, or 12 at a time. We want something that a trainer can pull up and Check in a client. This will record the date and time the client was checked in, by what trainer, and what type of session. This system will keep track of the following:
Whenever a Client Checks in so it will ‘tick off’ a session on their package (ie- they have gone from 11 sessions left to 10 sessions left)
Track what sessions a particular trainer does so we can pay them at the end of the week and look at who they trained, what type of session and how many
Look at client activity: Every time they check in, Recharge their package, any activity related to the client, even if it was admin – like deleting a session that was mistakenly recorded.
This will keep a database of clients added and all their activity
The pdf I have included lays out how I think it would work and the features I want
I would like this to run off an tablora that we have at our front check in counter. It can be an app or a URL that use.
***THIS PROJECT IS NOT SO MUCH ABOUT DESIGN BUT ABOUT FUNCTIONALITY OF THE APPLICATION. IT MUST HAVE THE FEATURES I HAVE ASKED FOR THAT WORK TOGETHER. I AM WILLING TO PAY A LITTLE MORE AS A BONUS IF YOU CAN ACCOMPLISH THIS. ALSO IF I FIN THE RIGHT PERSON THAT CAN DO THIS I WILL MAKE IT A GUARNTEED PROJECT.

- Functionality and Track and record all the info we need

```html
<!DOCTYPE html>
<html lang="en">
<head>
<meta charset="utf-8">
<title>Sessions Panel</title>
<link rel="stylesheet" href="https://fonts.googleapis.com/css2?family=Inter:wght@400;500;600;700&display=swap">
<style>
:root{
  --bg:#fafafa;
  --surface:#ffffff;
  --line:#e5e7eb;
  --ink:#111111;
  --ink-soft:#4b5563;
  --muted:#9ca3af;
  --accent:#d97706;
  --accent-bg:#f1f1f1;
  --danger:#dc2626;
}
*{box-sizing:border-box;margin:0;padding:0}
html,body{width:703px;height:1200px;overflow:hidden;background:var(--bg)}
body{font-family:"Inter",sans-serif;color:var(--ink)}
.board{position:absolute;left:0;top:0;width:1475px;height:2520px;transform:scale(.4766);transform-origin:0 0;background:var(--bg)}
.screen{position:absolute;left:0;width:1475px}
.topbar{position:absolute;left:0;top:0;width:1475px;height:70px;background:var(--surface);border-bottom:1px solid var(--line)}
.brand{position:absolute;left:26px;top:18px;display:flex;align-items:center;gap:10px;font-size:28px;font-weight:700;color:#3f3f46;letter-spacing:.5px}
.brand-dot{width:16px;height:16px;background:var(--accent)}
.avatar{position:absolute;left:1406px;top:17px;width:35px;height:35px;border-radius:50%;background:var(--ink);color:#fff;font-size:14px;display:flex;align-items:center;justify-content:center}
.nav{position:absolute;left:17px;top:103px;width:295px}
.nav-item{height:43px;margin-bottom:4.5px;display:flex;align-items:center;gap:14px;padding-left:10px;font-size:15px;font-weight:500;color:#1f2937;border-radius:8px}
.nav-item svg{width:23px;height:23px;stroke:#9ca3af;fill:none;stroke-width:1.5}
.nav-item.active{background:var(--accent-bg);color:var(--accent)}
.nav-item.active svg{stroke:var(--accent)}
.crumb{position:absolute;left:380px;top:104px;font-size:15px;color:#6b7280;display:flex;gap:14px}
.page-title{position:absolute;left:380px;top:134px;font-size:32px;font-weight:700;letter-spacing:-.5px}
.btn{position:absolute;display:flex;align-items:center;justify-content:center;gap:8px;border-radius:8px;font-size:15px;font-weight:600;color:#fff}
.btn-accent{background:var(--accent)}
.btn-danger{background:var(--danger)}
.btn-plain{background:var(--surface);color:var(--ink);border:1px solid var(--line)}
.card{position:absolute;left:380px;top:207px;width:1060px;height:492px;background:var(--surface);border:1px solid var(--line);border-radius:12px;overflow:hidden}
.search{position:absolute;left:732px;top:13px;width:264px;height:40px;border:1px solid var(--line);border-radius:8px;display:flex;align-items:center;gap:10px;padding-left:14px;font-size:15px;color:var(--muted)}
.filter-icon{position:absolute;left:1014px;top:22px}
.badge{position:absolute;left:1038px;top:10px;font-size:11px;color:var(--accent);font-weight:600}
.row{position:absolute;left:0;width:1060px;border-top:1px solid var(--line);font-size:15px}
.row span{position:absolute;top:50%;transform:translateY(-50%);white-space:nowrap}
.head{background:var(--bg);font-weight:600}
.chk{left:25px;width:19px;height:19px;border:1px solid #d1d5db;border-radius:4px;background:#fff}
.c1{left:69px}.c2{left:198px}.c3{left:324px}.c4{left:650px}.c5{left:843px}
.edit{left:986px;color:var(--accent);font-weight:600}
.caret{color:var(--muted);font-weight:400;margin-left:6px;font-size:12px}
.foot{position:absolute;left:0;top:426px;width:1060px;height:66px;border-top:1px solid var(--line)}
.foot-text{position:absolute;left:26px;top:23px;font-size:15px;color:#374151}
.perpage{position:absolute;left:450px;top:12px;width:160px;height:40px;border:1px solid var(--line);border-radius:8px;display:flex;font-size:15px}
.perpage b{font-weight:400;color:#6b7280;padding:10px 13px;border-right:1px solid var(--line)}
.perpage i{font-style:normal;padding:10px 13px}
.section-title{position:absolute;left:400px;top:745px;font-size:86px;font-weight:500;letter-spacing:-1px;z-index:2}
.label{position:absolute;font-size:15px;font-weight:500}
.label sup{color:var(--danger);font-size:10px}
.field{position:absolute;width:518px;height:41px;background:var(--surface);border:1px solid var(--line);border-radius:8px;display:flex;align-items:center;padding-left:13px;font-size:15px}
.field .tail{position:absolute;right:14px;color:#6b7280;font-size:13px;letter-spacing:14px}
.prefix{width:36px;height:100%;border-right:1px solid var(--line);display:flex;align-items:center;color:#6b7280;margin-left:-13px;padding-left:13px;margin-right:13px}
.filters{position:absolute;left:1069px;top:259px;width:345px;height:366px;background:var(--surface);border:1px solid var(--line);border-radius:12px;box-shadow:0 10px 25px rgba(0,0,0,.1)}
.filters h3{position:absolute;left:26px;top:29px;font-size:17px;font-weight:600}
.reset{position:absolute;right:26px;top:31px;font-size:15px;color:var(--danger);font-weight:600}
.filters .label{left:26px}
.select{position:absolute;left:26px;width:294px;height:41px;border:1px solid var(--line);border-radius:8px;font-size:15px;color:var(--muted);display:flex;align-items:center;padding-left:13px}
.select::after{content:"⌄";position:absolute;right:16px;top:6px;color:#374151}
</style>
</head>
<body>
<div class="board">

<!-- List screen -->
<section class="screen" style="top:0;height:720px">
  <header class="topbar"><div class="brand"><span class="brand-dot"></span>FORGEWELL</div><div class="avatar">A</div></header>
  <nav class="nav">
    <div class="nav-item"><svg viewBox="0 0 24 24"><path d="M3 11l9-7 9 7v9H3z"/><path d="M10 20v-5h4v5"/></svg>Dashboard</div>
    <div class="nav-item"><svg viewBox="0 0 24 24"><circle cx="12" cy="8" r="3"/><circle cx="5" cy="10" r="2.5"/><circle cx="19" cy="10" r="2.5"/><path d="M6 19c0-3 3-5 6-5s6 2 6 5M1 18c0-2 2-4 4-4M23 18c0-2-2-4-4-4"/></svg>Clients</div>
    <div class="nav-item active"><svg viewBox="0 0 24 24"><rect x="4" y="4" width="16" height="18" rx="2"/><rect x="8" y="2" width="8" height="4" rx="1"/><path d="M8 11h8M8 15h8M8 19h5"/></svg>Session Logs</div>
    <div class="nav-item"><svg viewBox="0 0 24 24"><rect x="3" y="3" width="7" height="7" rx="2"/><rect x="14" y="3" width="7" height="7" rx="2"/><rect x="3" y="14" width="7" height="7" rx="2"/><rect x="14" y="14" width="7" height="7" rx="2"/></svg>Session Types</div>
    <div class="nav-item"><svg viewBox="0 0 24 24"><circle cx="12" cy="12" r="10"/><circle cx="12" cy="10" r="3"/><path d="M6 19c1.5-3 3.5-4 6-4s4.5 1 6 4"/></svg>Trainers</div>
  </nav>
  <div class="crumb"><span>Session Logs</span><span>›</span><span>List</span></div>
  <h1 class="page-title">Session Logs</h1>
  <div class="btn btn-accent" style="left:1276px;top:134px;width:164px;height:39px"><svg width="18" height="18" viewBox="0 0 24 24" fill="none" stroke="#fff" stroke-width="2"><circle cx="12" cy="12" r="10"/><path d="M8 12l3 3 5-6"/></svg>Client Check In</div>
  <div class="card">
    <div class="search"><svg width="18" height="18" viewBox="0 0 24 24" fill="none" stroke="#9ca3af" stroke-width="2"><circle cx="11" cy="11" r="7"/><path d="M20 20l-4-4"/></svg>Search</div>
    <svg class="filter-icon" width="20" height="20" viewBox="0 0 24 24" fill="#6b7280"><path d="M2 3h20l-8 10v8l-4-2v-6z"/></svg><span class="badge">0</span>
    <div class="row head" style="top:66px;height:52px"><span class="chk"></span><span class="c1">Client<b class="caret">⌄</b></span><span class="c2">Trainer<b class="caret">⌄</b></span><span class="c3">Session type</span><span class="c4">Check in time<b class="caret">⌄</b></span><span class="c5">Pay amount<b class="caret">⌄</b></span></div>
    <div class="row" style="top:118px;height:61px"><span class="chk"></span><span class="c1">Olivia White</span><span class="c2">Alex Johnson</span><span class="c3">Partner Session</span><span class="c4">Jun 29, 2025 07:13:46</span><span class="c5">$60.00</span><span class="edit">✎ Edit</span></div>
    <div class="row" style="top:179px;height:62px"><span class="chk"></span><span class="c1">Sarah Wilson</span><span class="c2">Ben Davis</span><span class="c3">Single Session</span><span class="c4">Jun 29, 2025 07:13:30</span><span class="c5">$45.00</span><span class="edit">✎ Edit</span></div>
    <div class="row" style="top:241px;height:61px"><span class="chk"></span><span class="c1">Michael Miller</span><span class="c2">Chloe Green</span><span class="c3">Single Session</span><span class="c4">Jun 29, 2025 07:13:18</span><span class="c5">$45.00</span><span class="edit">✎ Edit</span></div>
    <div class="row" style="top:302px;height:62px"><span class="chk"></span><span class="c1">Olivia White</span><span class="c2">Dan Smith</span><span class="c3">Partner Session (Only 1 Partner Showed)</span><span class="c4">Jun 29, 2025 07:08:25</span><span class="c5">$45.00</span><span class="edit">✎ Edit</span></div>
    <div class="row" style="top:364px;height:62px"><span class="chk"></span><span class="c1">John Doe</span><span class="c2">Chloe Green</span><span class="c3">Partner Session</span><span class="c4">Jun 29, 2025 07:05:55</span><span class="c5">$60.00</span><span class="edit">✎ Edit</span></div>
    <div class="foot"><span class="foot-text">Showing 1 to 5 of 5 results</span><div class="perpage"><b>Per page</b><i>10 ⌄</i></div></div>
  </div>
</section>

<h2 class="section-title">5. Sessions Panel</h2>

<!-- Edit screen -->
<section class="screen" style="top:797px;height:600px">
  <header class="topbar"><div class="brand"><span class="brand-dot"></span>FORGEWELL</div><div class="avatar">A</div></header>
  <nav class="nav">
    <div class="nav-item"><svg viewBox="0 0 24 24"><path d="M3 11l9-7 9 7v9H3z"/><path d="M10 20v-5h4v5"/></svg>Dashboard</div>
    <div class="nav-item"><svg viewBox="0 0 24 24"><circle cx="12" cy="8" r="3"/><circle cx="5" cy="10" r="2.5"/><circle cx="19" cy="10" r="2.5"/><path d="M6 19c0-3 3-5 6-5s6 2 6 5M1 18c0-2 2-4 4-4M23 18c0-2-2-4-4-4"/></svg>Clients</div>
    <div class="nav-item active"><svg viewBox="0 0 24 24"><rect x="4" y="4" width="16" height="18" rx="2"/><rect x="8" y="2" width="8" height="4" rx="1"/><path d="M8 11h8M8 15h8M8 19h5"/></svg>Session Logs</div>
    <div class="nav-item"><svg viewBox="0 0 24 24"><rect x="3" y="3" width="7" height="7" rx="2"/><rect x="14" y="3" width="7" height="7" rx="2"/><rect x="3" y="14" width="7" height="7" rx="2"/><rect x="14" y="14" width="7" height="7" rx="2"/></svg>Session Types</div>
    <div class="nav-item"><svg viewBox="0 0 24 24"><circle cx="12" cy="12" r="10"/><circle cx="12" cy="10" r="3"/><path d="M6 19c1.5-3 3.5-4 6-4s4.5 1 6 4"/></svg>Trainers</div>
  </nav>
  <div class="crumb"><span>Session Logs</span><span>›</span><span>Edit</span></div>
  <h1 class="page-title">Edit Session Log</h1>
  <div class="btn btn-danger" style="left:1368px;top:134px;width:72px;height:39px">Delete</div>
  <div class="label" style="left:380px;top:211px">Client<sup>*</sup></div>
  <div class="field" style="left:380px;top:242px">Olivia White<span class="tail">✕⌄</span></div>
  <div class="label" style="left:923px;top:211px">Trainer<sup>*</sup></div>
  <div class="field" style="left:923px;top:242px">Alex Johnson<span class="tail">✕⌄</span></div>
  <div class="label" style="left:380px;top:310px">Session type<sup>*</sup></div>
  <div class="field" style="left:380px;top:341px">Partner Session<span class="tail">⌄</span></div>
  <div class="label" style="left:923px;top:310px">Check in time<sup>*</sup></div>
  <div class="field" style="left:923px;top:341px">06/29/2025 07:13:46 AM<span class="tail">▣</span></div>
  <div class="label" style="left:380px;top:410px">Pay amount<sup>*</sup></div>
  <div class="field" style="left:380px;top:440px"><span class="prefix">$</span>60</div>
  <div class="label" style="left:923px;top:410px">Partner</div>
  <div class="field" style="left:923px;top:440px">David Taylor<span class="tail">✕⌄</span></div>
  <div class="btn btn-accent" style="left:380px;top:506px;width:128px;height:38px">Save changes</div>
  <div class="btn btn-plain" style="left:521px;top:506px;width:77px;height:38px">Cancel</div>
</section>

<!-- List screen with filters -->
<section class="screen" style="top:1413px;height:720px">
  <header class="topbar"><div class="brand"><span class="brand-dot"></span>FORGEWELL</div><div class="avatar">A</div></header>
  <nav class="nav">
    <div class="nav-item"><svg viewBox="0 0 24 24"><path d="M3 11l9-7 9 7v9H3z"/><path d="M10 20v-5h4v5"/></svg>Dashboard</div>
    <div class="nav-item"><svg viewBox="0 0 24 24"><circle cx="12" cy="8" r="3"/><circle cx="5" cy="10" r="2.5"/><circle cx="19" cy="10" r="2.5"/><path d="M6 19c0-3 3-5 6-5s6 2 6 5M1 18c0-2 2-4 4-4M23 18c0-2-2-4-4-4"/></svg>Clients</div>
    <div class="nav-item active"><svg viewBox="0 0 24 24"><rect x="4" y="4" width="16" height="18" rx="2"/><rect x="8" y="2" width="8" height="4" rx="1"/><path d="M8 11h8M8 15h8M8 19h5"/></svg>Session Logs</div>
    <div class="nav-item"><svg viewBox="0 0 24 24"><rect x="3" y="3" width="7" height="7" rx="2"/><rect x="14" y="3" width="7" height="7" rx="2"/><rect x="3" y="14" width="7" height="7" rx="2"/><rect x="14" y="14" width="7" height="7" rx="2"/></svg>Session Types</div>
    <div class="nav-item"><svg viewBox="0 0 24 24"><circle cx="12" cy="12" r="10"/><circle cx="12" cy="10" r="3"/><path d="M6 19c1.5-3 3.5-4 6-4s4.5 1 6 4"/></svg>Trainers</div>
  </nav>
  <div class="crumb"><span>Session Logs</span><span>›</span><span>List</span></div>
  <h1 class="page-title">Session Logs</h1>
  <div class="btn btn-accent" style="left:1276px;top:134px;width:164px;height:39px"><svg width="18" height="18" viewBox="0 0 24 24" fill="none" stroke="#fff" stroke-width="2"><circle cx="12" cy="12" r="10"/><path d="M8 12l3 3 5-6"/></svg>Client Check In</div>
  <div class="card">
    <div class="search"><svg width="18" height="18" viewBox="0 0 24 24" fill="none" stroke="#9ca3af" stroke-width="2"><circle cx="11" cy="11" r="7"/><path d="M20 20l-4-4"/></svg>Search</div>
    <svg class="filter-icon" width="20" height="20" viewBox="0 0 24 24" fill="#6b7280"><path d="M2 3h20l-8 10v8l-4-2v-6z"/></svg><span class="badge">0</span>
    <div class="row head" style="top:66px;height:52px"><span class="chk"></span><span class="c1">Client<b class="caret">⌄</b></span><span class="c2">Trainer<b class="caret">⌄</b></span><span class="c3">Session type</span><span class="c4">Check in time</span></div>
    <div class="row" style="top:118px;height:61px"><span class="chk"></span><span class="c1">Olivia White</span><span class="c2">Alex Johnson</span><span class="c3">Partner Session</span><span class="c4">Jun 29</span></div>
    <div class="row" style="top:179px;height:62px"><span class="chk"></span><span class="c1">Sarah Wilson</span><span class="c2">Ben Davis</span><span class="c3">Single Session</span><span class="c4">Jun 29</span></div>
    <div class="row" style="top:241px;height:61px"><span class="chk"></span><span class="c1">Michael Miller</span><span class="c2">Chloe Green</span><span class="c3">Single Session</span><span class="c4">Jun 29</span></div>
    <div class="row" style="top:302px;height:62px"><span class="chk"></span><span class="c1">Olivia White</span><span class="c2">Dan Smith</span><span class="c3">Partner Session (Only 1 Partner Showed)</span><span class="c4">Jun 29</span></div>
    <div class="row" style="top:364px;height:62px"><span class="chk"></span><span class="c1">John Doe</span><span class="c2">Chloe Green</span><span class="c3">Partner Session</span><span class="c4">Jun 29</span></div>
    <div class="foot"><span class="foot-text">Showing 1 to 5 of 5 results</span><div class="perpage"><b>Per page</b><i>10 ⌄</i></div></div>
  </div>
  <div class="filters">
    <h3>Filters</h3><span class="reset">Reset</span>
    <div class="label" style="top:73px">Trainer</div>
    <div class="select" style="top:104px">All</div>
    <div class="label" style="top:172px">Session type</div>
    <div class="select" style="top:203px">All</div>
    <div class="label" style="top:271px">Period</div>
    <div class="select" style="top:302px;color:var(--ink)">All</div>
  </div>
</section>

</div>
</body>
</html>
```